Best in class business looking for best in class stationery that accurately reflects the brand image we are trying to build as the brand expands throughout the country. The Varying items should be an eye catching design that makes even the simplest letter or small business card stand out in the crowd.

Target Market(s)

Professionals

Industry/Entity Type

Real Estate

Other font styles liked:
• See atttached logo

Requirements
Must have
• Letterhead
• Business cards
• Envelopes
• Labels for larger mailings
Nice to have
• Folders
• Notebook
Should not have
• Stale design elements

```html
<!DOCTYPE html>
<html lang="en">
<head>
<meta charset="utf-8">
<title>Alder Peak Holdings — Business Card</title>
<link href="https://fonts.googleapis.com/css2?family=Cinzel:wght@500&display=swap" rel="stylesheet">
<style>
  :root {
    --backdrop: #e4e4e4;
    --card-navy: #263579;
    --bar-blue: #2f57a6;
    --ink-white: #ffffff;
  }
  * { margin: 0; padding: 0; box-sizing: border-box; }
  html, body {
    width: 1200px;
    height: 800px;
    overflow: hidden;
    background: var(--backdrop);
  }
  .business-card {
    position: absolute;
    left: 30px;
    top: 67px;
    width: 1140px;
    height: 666px;
    background: var(--card-navy);
    overflow: hidden;
  }
  .card-bars {
    position: absolute;
    inset: 0;
    width: 100%;
    height: 100%;
  }
  .card-bars polygon { fill: var(--bar-blue); }
  .brand-block {
    position: absolute;
    left: 745px;
    top: 300px;
    transform: translateX(-50%);
    display: flex;
    flex-direction: column;
    align-items: center;
    gap: 34px;
  }
  .brand-mark {
    width: 46px;
    height: 46px;
    background: var(--ink-white);
  }
  .brand-name {
    font-family: "Cinzel", "Times New Roman", serif;
    font-weight: 500;
    font-size: 42px;
    letter-spacing: 1px;
    color: var(--ink-white);
    white-space: nowrap;
  }
</style>
</head>
<body>
  <div class="business-card">
    <svg class="card-bars" viewBox="0 0 522 305" preserveAspectRatio="none" aria-hidden="true">
      <polygon points="10,40 32,54 32,305 10,305"/>
      <polygon points="58,72 80,86 80,305 58,305"/>
      <polygon points="106,104 128,118 128,305 106,305"/>
      <polygon points="153,135 175,149 175,305 153,305"/>
    </svg>
    <div class="brand-block">
      <div class="brand-mark"></div>
      <p class="brand-name">Alder Peak Holdings</p>
    </div>
  </div>
</body>
</html>
```